International freight forwarder experienced in perishable handling needs a web design

We need a website designed that will allow us to capture more customers through the website. We would like a visually appealing design that is not so heavy on text. Our business covers the logistics and freight forwarding industries and we have offices in South America and the USA. Our main customers are importers USA, Europe, Asia and Russia and we currently work almost exclusively with perishable products such as fresh cut flowers, fresh exotics fruits, cacao, fresh fish etc. We would like to convey a fresh, modern approach to freight forwarding focusing on concepts such as - time sensitive, anytime-anywhere delivery, innovation, experience, reliability and confidence. Should include links with Plumetta and Worvanet. Our core solutions include: Core Services
*Air Freight
*Ocean Freight
*Warehousing & Distribution
Our industry solutions cover
*Flowers
*FMCG including, fruits, vegetables
*Live animals
*Automotive
*Consumer Goods
*Industrial
*Oil & Gas
*Pharma
* Event logistics
* Project logistics

Target Market(s)

Importers in Europe, USA, Asia, Middle East and Russia

Number of Pages Required

4 page

Font styles to use
Sans Serif

Colors
a1cd39
606060
000000

Requirements
Must have
• Photos of fresh cut flowers, FMCG such as cacao, fresh fish (packaged for shipping), fresh exotic fruits, pharma products (packaged for shipping), oil and gas etc. Internal customer login access
Nice to have
• Photos of cargo shipping carriers and cargo airline carriers. Features similar to those of following website http://www.brolvacargo.com/eng/main/index.jsp?FromURL=web
Should not have
• Too much text, needs to be visually pleasing

```html
<!DOCTYPE html>
<html lang="en">
<head>
<meta charset="utf-8">
<title>Verdanta Freight</title>
<link href="https://fonts.googleapis.com/css2?family=Nunito+Sans:wght@300;400;600;700;800&family=Open+Sans:wght@300;700&display=swap" rel="stylesheet">
<style>
:root{
  --green:#a1cd39;
  --green-dark:#8fb92c;
  --grey:#606060;
  --ink:#000;
  --light:#e8e8e8;
  --footer:#3a3a3a;
  --footer-bottom:#232323;
  --muted:#8a8a8a;
}
*{margin:0;padding:0;box-sizing:border-box}
html,body{width:765px;height:1200px;overflow:hidden;background:#fff}
body{position:relative;font-family:"Nunito Sans",Arial,sans-serif;color:var(--grey)}
.abs{position:absolute}
a{color:inherit;text-decoration:none}

/* header */
.header{left:0;top:0;width:765px;height:77px;background:#fff;z-index:3;box-shadow:0 1px 3px rgba(0,0,0,.15)}
.brand{left:63px;top:26px;display:flex;align-items:center;gap:6px}
.brand-dot{width:26px;height:26px;border-radius:50%;background:var(--green)}
.brand-name{font-size:19px;font-weight:700;color:var(--grey);letter-spacing:-.3px}
.brand-sub{left:96px;top:53px;font-size:8px;letter-spacing:4px;color:var(--muted)}
.follow{left:436px;top:13px;font-size:9px;color:var(--muted)}
.social{top:11px;width:14px;height:14px;border:1px solid #b5b5b5;border-radius:50%}
.lang{left:570px;top:9px;width:60px;height:19px;border:1px solid #c8c8c8;font-size:9px;color:var(--muted);display:flex;align-items:center;gap:5px;padding-left:5px}
.lang i{width:14px;height:9px;background:#c9c9d6;display:block}
.login{left:641px;top:9px;width:41px;height:19px;background:var(--green);color:#fff;font-size:9px;font-weight:800;display:flex;align-items:center;justify-content:center}
.nav{top:46px;font-size:10.5px;color:#222}
.nav-active{left:352px;top:42px;width:105px;height:22px;background:var(--green);color:#fff;font-size:10.5px;display:flex;align-items:center;justify-content:center}

/* hero */
.hero{left:0;top:77px;width:765px;height:289px;background:linear-gradient(100deg,#c9b49a 0%,#e2c9a4 35%,#b78a5c 55%,#6b4d36 80%,#3b3029 100%)}
.hero-kicker{left:62px;top:180px;font-family:"Open Sans",sans-serif;font-weight:300;font-size:22px;color:#222}
.hero-title{left:61px;top:205px;font-family:"Open Sans",sans-serif;font-weight:700;font-size:31px;color:#111}
.hero-dot{top:343px;width:8px;height:8px;border-radius:50%;background:#555;border:1px solid #999}
.dropdown{left:352px;top:65px;width:129px;z-index:4}
.dropdown div{height:21.5px;background:var(--green);color:#fff;font-size:8.5px;padding-left:7px;display:flex;align-items:center;border-bottom:1px solid rgba(255,255,255,.25)}
.dropdown .current{background:#444}

/* services */
.map{left:70px;top:380px;width:612px;height:295px;background:radial-gradient(ellipse at center,#f0f0f0 0%,#fafafa 60%,#fff 100%)}
.section-title{width:765px;left:0;text-align:center;font-size:27px;font-weight:400;color:#444}
.section-title span{color:var(--green)}
.section-lead{left:150px;width:465px;text-align:center;font-size:9.5px;line-height:15.5px;color:var(--grey)}
.service{width:170px;text-align:center}
.service svg{display:block;margin:0 auto}
.service h3{font-size:13.5px;font-weight:700;color:#444;margin-top:7px;line-height:17px}
.service p{font-size:8.2px;line-height:15px;color:var(--grey);margin-top:8px}

/* industries */
.industries{left:0;top:681px;width:765px;height:286px;background:var(--light)}
.card{top:818px;width:198px;height:109px;display:flex;align-items:center;justify-content:center;text-align:center;color:#fff;font-weight:800;font-size:14px;line-height:15px;text-shadow:0 1px 3px rgba(0,0,0,.5)}
.card-flowers{left:71px;background:linear-gradient(135deg,#6b6a45,#a35a45 50%,#5d6b3c)}
.card-fmcg{left:286px;background:linear-gradient(135deg,#b88c3c,#d9b04a 50%,#8a5a2a)}
.card-animals{left:498px;background:linear-gradient(135deg,#6e7585,#9aa1af 50%,#5a6070)}
.mini-dot{top:941px;width:4px;height:4px;border-radius:50%;background:#555}

/* footer */
.footer{left:0;top:967px;width:765px;height:201px;background:var(--footer)}
.footer h4{font-size:14.5px;font-weight:400;color:#e0e0e0}
.footer-text{font-size:7.8px;line-height:12.8px;color:#7a7a7a;width:170px}
.footer-links li{list-style:none;font-size:8px;color:#8a8a8a;height:16px}
.contact-line{left:575px;font-size:8.3px;color:#bdbdbd;line-height:15.3px;width:130px}
.bottom{left:0;top:1168px;width:765px;height:32px;background:var(--footer-bottom);font-size:8.5px;color:#e0e0e0}
</style>
</head>
<body>

<header class="abs header">
  <div class="abs brand"><span class="brand-dot"></span><span class="brand-name">Verdanta Freight</span></div>
  <div class="abs brand-sub">GROUP</div>
  <div class="abs follow">Follow Us On</div>
  <span class="abs social" style="left:500px"></span>
  <span class="abs social" style="left:520px"></span>
  <span class="abs social" style="left:540px"></span>
  <div class="abs lang"><i></i>English</div>
  <a class="abs login" href="#">LOGIN</a>
  <a class="abs nav" style="left:303px" href="#">About Us</a>
  <a class="abs nav-active" href="#">Products &amp; Services</a>
  <a class="abs nav" style="left:467px" href="#">Industry Tailored Solutions</a>
  <a class="abs nav" style="left:598px" href="#">Network</a>
  <a class="abs nav" style="left:648px" href="#">Contact</a>
</header>

<section class="abs hero" role="img" aria-label="Freight truck driving on a city road at sunset"></section>
<div class="abs hero-kicker">Fast &amp; Accurate Freight</div>
<div class="abs hero-title">Verdanta Freight</div>
<span class="abs hero-dot" style="left:359px;background:#888"></span>
<span class="abs hero-dot" style="left:370px"></span>
<span class="abs hero-dot" style="left:382px"></span>

<nav class="abs dropdown">
  <div class="current">Air Freight</div>
  <div>Sea Freight</div>
  <div>Road</div>
  <div>Express</div>
  <div>Warehousing &amp; Distribution</div>
  <div>Innovation &amp; E-Commerce</div>
</nav>

<div class="abs map" role="img" aria-label="Faint dotted world map"></div>
<h2 class="abs section-title" style="top:401px">International Freight <span>Forwarding</span></h2>
<p class="abs section-lead" style="top:442px">Lorem ipsum dolor sit amet, consectetur adipiscing elit, sed do eiusmod tempor incididunt ut labore et dolore magna aliqua. Ut enim ad minim veniam, quis nostrud exercitation ullamco.</p>

<div class="abs service" style="left:67px;top:493px">
  <svg width="62" height="62" viewBox="0 0 62 62"><circle cx="31" cy="31" r="29" fill="none" stroke="var(--green)" stroke-width="2"/><path d="M16 37l5-1 5-4-6-7 3-1 9 5 8-5c3-2 6-1 5 1l-7 6 -3 10-3 1 0-8-8 5-7 1z" fill="var(--green)"/></svg>
  <h3>AIR FREIGHT</h3>
  <p>Lorem ipsum dolor sit amet, con sec tetur adipiscing elit. sed do.</p>
</div>
<div class="abs service" style="left:294px;top:493px">
  <svg width="62" height="62" viewBox="0 0 62 62"><circle cx="31" cy="31" r="29" fill="none" stroke="var(--green)" stroke-width="2"/><rect x="28" y="15" width="4" height="8" fill="var(--green)"/><rect x="22" y="23" width="16" height="8" fill="var(--green)"/><path d="M15 32h32l-5 9H20z" fill="var(--green)"/><path d="M16 44c4 2 6 2 10 0s6-2 10 0 6 2 10 0" stroke="var(--green)" stroke-width="2" fill="none"/></svg>
  <h3>OCEAN FREIGHT</h3>
  <p style="margin-top:4px">Lorem ipsum dolor sit amet, con sec tetur adipiscing elit. sed do.</p>
</div>
<div class="abs service" style="left:506px;top:493px">
  <svg width="62" height="62" viewBox="0 0 62 62"><circle cx="31" cy="31" r="29" fill="none" stroke="var(--green)" stroke-width="2"/><rect x="15" y="20" width="19" height="19" rx="2" fill="var(--green)"/><path d="M35 25h7l5 7v7H35z" fill="var(--green)"/><circle cx="22" cy="41" r="4" fill="var(--green)" stroke="#fff" stroke-width="1.5"/><circle cx="41" cy="41" r="4" fill="var(--green)" stroke="#fff" stroke-width="1.5"/></svg>
  <h3>WAREHOUSING<br>&amp; DISTRIBUTION</h3>
  <p>Lorem ipsum dolor sit amet, con sec tetur adipiscing elit. sed do.</p>
</div>

<section class="abs industries"></section>
<h2 class="abs section-title" style="top:712px">Industry Specific <span>Solutions</span></h2>
<p class="abs section-lead" style="top:752px">Lorem ipsum dolor sit amet, consectetur adipiscing elit, sed do eiusmod tempor incididunt ut labore et dolore magna aliqua. Ut enim ad minim veniam, quis nostrud exercitation ullamco.</p>
<svg class="abs" style="left:42px;top:871px" width="12" height="14" viewBox="0 0 12 14"><path d="M9 1L3 7l6 6" stroke="#444" stroke-width="3" fill="none"/></svg>
<svg class="abs" style="left:706px;top:866px" width="12" height="14" viewBox="0 0 12 14"><path d="M3 1l6 6-6 6" stroke="#444" stroke-width="3" fill="none"/></svg>
<div class="abs card card-flowers" role="img" aria-label="Bouquets of fresh cut flowers in crates">FLOWERS</div>
<div class="abs card card-fmcg" role="img" aria-label="Market display of fresh fruits and vegetables">FMCG INCLUDING,<br>FRUITS, VEGETABLES</div>
<div class="abs card card-animals" role="img" aria-label="Fresh fish packed for shipping">LIVE ANIMALS</div>
<span class="abs mini-dot" style="left:375px;background:#999"></span>
<span class="abs mini-dot" style="left:381px"></span>
<span class="abs mini-dot" style="left:387px"></span>

<footer class="abs footer">
  <h4 class="abs" style="left:71px;top:24px">About Us</h4>
  <p class="abs footer-text" style="left:71px;top:54px">Lorem ipsum dolor amet consectetur adipisic-ing elit, sed do eiusmod tempor incididunt ut labore et dolore magna aliqua ut enim ad minim veniam, quis nostrud exercitation. ullamco laboris nisi ut aliquip ex ea commodo consequat.</p>
  <h4 class="abs" style="left:346px;top:26px">Navigation</h4>
  <ul class="abs footer-links" style="left:347px;top:55px">
    <li>Home</li><li>About us</li><li>International Freight Forwarding</li><li>Industry Specific Solutions</li><li>Supply Chain Solutions</li><li>Contact us</li>
  </ul>
  <h4 class="abs" style="left:575px;top:26px">Contact Us</h4>
  <svg class="abs" style="left:557px;top:59px" width="11" height="8" viewBox="0 0 11 8"><rect width="11" height="8" fill="#ddd"/><path d="M0 0l5.5 4.5L11 0" stroke="#3a3a3a" fill="none"/></svg>
  <svg class="abs" style="left:557px;top:73px" width="12" height="12" viewBox="0 0 12 12"><path d="M2 1l2.5-.5 1.5 3-1.5 1.2c.7 1.5 1.8 2.6 3.3 3.3L9 6.5l3 1.5-.5 2.5C5 11 1 7 2 1z" fill="#ddd"/></svg>
  <svg class="abs" style="left:558px;top:118px" width="9" height="13" viewBox="0 0 9 13"><path d="M4.5 0A4.5 4.5 0 0 0 0 4.5C0 8 4.5 13 4.5 13S9 8 9 4.5A4.5 4.5 0 0 0 4.5 0z" fill="#ddd"/><circle cx="4.5" cy="4.5" r="1.7" fill="#3a3a3a"/></svg>
  <div class="abs contact-line" style="top:54px">ops@verdantafreight.com<br>+593 (99) 555 0142<br>+593 (2) 555 0187<br>/ 555 0190 / 555 0193</div>
  <div class="abs contact-line" style="top:116px">Av. Horizonte 12-40<br>Edificio Mirador<br>Center - Floors 2 &amp; 3<br>Tumbaco - Quito - Ecuador</div>
</footer>

<div class="abs bottom">
  <span class="abs" style="left:71px;top:10px">© Copyright verdantafreightcargo.com.All Right Reserved.</span>
  <span class="abs" style="left:553px;top:10px">Terms &amp; Condition &nbsp;&nbsp;|&nbsp;&nbsp; Privacy Policy</span>
</div>

</body>
</html>
```